Australian IT Company requires Business Card Design

Bluewattle is an Australian company that specialises in IT consulting & support, software development, project management, network services.

We have been in business for 15 years.

* We require a business card with the following on it:
Logo
Address
Contact Details
Space for staff name, title & mobile number

Industry/Entity Type

Software

```html
<!DOCTYPE html>
<html lang="en">
<head>
<meta charset="utf-8">
<title>Bluewattle Business Card</title>
<link rel="stylesheet" href="https://fonts.googleapis.com/css2?family=Montserrat:wght@300;400;600&family=Arimo:wght@400&display=swap">
<style>
  :root {
    --brand-blue: #3a6b98;
    --ink: #2b2b2b;
    --muted: #6d6f72;
    --card-white: #ffffff;
    --page-bg: #e9ebee;
  }
  html, body {
    margin: 0;
    width: 1200px;
    height: 900px;
    overflow: hidden;
    background: var(--page-bg);
  }
  .card {
    position: absolute;
    left: 100px;
    top: 144px;
    width: 1000px;
    height: 612px;
    background: var(--card-white);
    box-shadow: 0 6px 24px rgba(0,0,0,0.15);
    overflow: hidden;
  }
  .brand {
    position: absolute;
    left: 150px;
    top: 150px;
    display: flex;
    align-items: center;
    gap: 26px;
  }
  .brand-mark {
    width: 92px;
    height: 92px;
    background: var(--brand-blue);
  }
  .brand-name {
    font-family: "Montserrat", sans-serif;
    font-weight: 600;
    font-size: 66px;
    letter-spacing: 1px;
    line-height: 1;
    color: var(--brand-blue);
    margin: 0;
  }
  .brand-tagline {
    font-family: "Montserrat", sans-serif;
    font-weight: 400;
    font-size: 15px;
    letter-spacing: 7.4px;
    color: var(--muted);
    margin: 10px 0 0 4px;
    text-transform: uppercase;
    white-space: nowrap;
  }
  .staff {
    position: absolute;
    left: 150px;
    top: 345px;
  }
  .staff-name {
    font-family: "Montserrat", sans-serif;
    font-weight: 300;
    font-size: 42px;
    color: var(--ink);
    margin: 0;
    letter-spacing: 1px;
  }
  .staff-title {
    font-family: "Montserrat", sans-serif;
    font-weight: 300;
    font-size: 30px;
    color: var(--brand-blue);
    margin: 2px 0 0 90px;
  }
  .divider {
    position: absolute;
    left: 545px;
    top: 300px;
    width: 1px;
    height: 150px;
    background: var(--brand-blue);
  }
  .contact {
    position: absolute;
    left: 585px;
    top: 290px;
    font-family: "Arimo", sans-serif;
    font-size: 20px;
    line-height: 1.45;
    color: var(--ink);
    margin: 0;
  }
  .contact dt {
    float: left;
    clear: left;
    width: 90px;
    text-align: right;
    margin-right: 6px;
    color: var(--brand-blue);
  }
  .contact dd { margin: 0 0 0 96px; }
  .web-band {
    position: absolute;
    left: 0;
    bottom: 0;
    width: 100%;
    height: 84px;
    background: var(--brand-blue);
    display: flex;
    align-items: center;
    justify-content: center;
    font-family: "Montserrat", sans-serif;
    font-size: 28px;
    letter-spacing: 18px;
    color: var(--card-white);
  }
</style>
</head>
<body>
  <article class="card">
    <header class="brand">
      <div class="brand-mark"></div>
      <div>
        <h1 class="brand-name">BLUEWATTLE</h1>
        <p class="brand-tagline">Reliable IT for growing teams</p>
      </div>
    </header>

    <section class="staff">
      <h2 class="staff-name">LIAM CARTER</h2>
      <p class="staff-title">Director</p>
    </section>

    <div class="divider"></div>

    <dl class="contact">
      <dt>phone:</dt><dd>+61 3 9555 0142</dd>
      <dt>email:</dt><dd>contact@bluewattle.net.au</dd>
      <dt>address:</dt><dd>14 Fern Lane<br>Unit 3<br>Kelvale Vic 3099</dd>
    </dl>

    <footer class="web-band">www.bluewattle.net.au</footer>
  </article>
</body>
</html>
```